Large corporation needs landing page for its employees with emotional and psychological problems

Vision:
Hello, we are a startup and would like to build a landing page and website in the mental health sector for a large corporation. In this site employees with emotional and psychological problems should quickly receive professional psychological support. This support takes the form of internal referrals from employees who are looking for help to qualified therapists, so that help can be provided quickly.
Furthermore, the employees get access to a tool where they can find out about topics in the mind health area and can also get help via webinars and podcasts. The employee should thus be able to take the hurdle to seek help and support in good time.
Therapists for whom the focus is on the urgency of providing quick help and support will work here in cooperation with the respective corporations.
Keywords:
• Help/Support
• overcome inhibitions
• Competent help
• Uncomplicated help
• Permanent access
• protected space
• Recognizing and naming emotional problems and actively tackling them
• get help
• mindfulness
• everyday helper
• Informative
• Anonymous
• compassion
• tolerance
• respect
• Appreciation
• empathy
• mindfulness
• protected space
• To be needed
• Like a lighthouse signal
What we need:
Landingpage
We need a landing page aimed at getting employees to contact psychological help. The call to action is to get in contact via a contact form.
Landing page content
There are several text modules:
• A heading/greeting
• A body of text at the beginning that explains the purpose of the page
• A bulleted text area describing the pain points and the solutions to them
Video:
The heart of the content will be a video explaining the need and inviting them to get in touch.
contact form:
It should be kept simple: first name, last name and email address
Legally required content:
General terms and conditions, data protection and imprint. These are only given as links in the footer.
In parallel, the Corporate Design should be adapted/extended:
Logo:
The font in the logo should be revised. The wings in the background remain.
Please adapt the logo for different uses:
• on a black background
• with transparent background
• favorite icon (browser)
• In square format for social media
Colors:
• develop a color chart based on the colors of the logo.
• please determine 2-3 main colors and the matching variations. I.e. transparent variations or light colors.
Typography:
Determine a decorative font and/or typography for headings and a text font. There should be no more than 3 fonts.
Industry/Entity Type
to recruit therapists as employees
Requirements
Should not have
- please not to playful design or typography - and max. 3 colors

```html
<!DOCTYPE html>
<html lang="en">
<head>
<meta charset="utf-8">
<title>Still Harbor – Support for Employees</title>
<link href="https://fonts.googleapis.com/css2?family=Roboto:ital,wght@0,400;0,500;0,700;1,400&display=swap" rel="stylesheet">
<style>
:root{
  --teal:#0d5a63;
  --teal-dark:#0a4c54;
  --sky:#b3dce6;
  --sky-soft:#d9eef3;
  --ink:#1d2b3a;
  --text:#33404a;
  --white:#ffffff;
  --mist:#eef2f4;
}
*{margin:0;padding:0;box-sizing:border-box}
html,body{width:1200px;height:4147px;overflow:hidden}
body{position:relative;font-family:"Roboto",Arial,sans-serif;color:var(--text);background:var(--white)}
.abs{position:absolute}
.brand{font-weight:500;color:var(--teal);font-size:40px;letter-spacing:-.5px;display:flex;align-items:center;gap:10px}
.brand-dot{width:14px;height:14px;border-radius:50%;background:var(--sky)}
.nav{display:flex;gap:0;font-size:14px;color:var(--teal)}
.nav a{color:inherit;text-decoration:none}
.btn{display:inline-flex;align-items:center;justify-content:center;font-size:14px;font-weight:500;text-decoration:none;border-radius:0 22px 0 22px}
.btn-dark{background:var(--teal);color:var(--white)}
.btn-light{background:var(--sky);color:var(--teal)}
.photo{border-radius:22px}
h2{font-weight:700;color:var(--teal);letter-spacing:-.5px}
p{line-height:1.45}

/* header */
.site-header{left:0;top:0;width:1200px;height:90px;z-index:5}
.site-header .brand{position:absolute;left:108px;top:28px}
.site-header .nav{position:absolute;left:400px;top:40px}
.site-header .nav a{margin-right:46px}
.quote-btn{position:absolute;left:975px;top:24px;width:122px;height:47px}

/* hero */
.hero-photo{left:0;top:0;width:1200px;height:760px;background:linear-gradient(120deg,#e6e4df 0%,#cfc9c0 35%,#9b9a95 60%,#b9b6b0 100%)}
.hero-circle{left:669px;top:362px;width:340px;height:340px;border-radius:50%;background:rgba(13,90,99,.92);color:var(--white);text-align:center}
.hero-circle h1{font-size:62px;font-weight:700;line-height:1;margin-top:72px}
.hero-circle .btn{width:124px;height:42px;margin-top:26px;font-size:12px;font-weight:400;border-radius:0 14px 0 14px}

/* about */
.about-bg{left:0;top:820px;width:1200px;height:622px;background:linear-gradient(180deg,#fff 0%,#f3f8fa 55%,#cfe6ee 85%,#a9d1de 100%)}
.about-photo{left:114px;top:912px;width:463px;height:383px;background:linear-gradient(135deg,#7b6a68 0%,#b9b3ad 55%,#6e6f72 100%)}
.about-title{left:617px;top:938px;font-size:56px}
.about-text{left:617px;top:1012px;width:432px;font-size:13.5px;color:var(--ink);line-height:1.44}
.about-btn{left:617px;top:1219px;width:122px;height:47px}

/* solutions */
.sol-title{left:0;top:1560px;width:1200px;text-align:center;font-size:54px}
.sol-text{left:270px;top:1638px;width:660px;text-align:center;font-size:13.5px;color:var(--ink)}
.sol-card{width:372px;height:128px;background:var(--white);border-radius:0 40px 0 40px;box-shadow:0 4px 18px rgba(20,60,70,.1)}
.sol-card h3{position:absolute;font-size:19px;font-weight:700;color:var(--ink);top:36px}
.sol-card p{position:absolute;font-size:12.5px;color:var(--ink);top:64px;width:200px;line-height:1.35}
.sol-card .icon{position:absolute;top:24px;width:82px;height:82px;border-radius:50%;display:flex;align-items:center;justify-content:center}
.sol-left h3,.sol-left p{right:126px;text-align:right}
.sol-left .icon{right:22px}
.sol-right h3,.sol-right p{left:126px}
.sol-right .icon{left:22px}
.icon.light{background:var(--sky)}
.icon.dark{background:var(--teal)}

/* video */
.video-bg{left:0;top:2050px;width:1200px;height:600px;background:linear-gradient(180deg,#fff 0%,#eef1f3 25%,#e7ebee 60%,#fff 100%)}
.video-title{left:151px;top:2180px;font-size:54px}
.video-text{left:153px;top:2255px;width:360px;font-size:13.5px;color:var(--ink)}
.video-btn{left:153px;top:2400px;width:122px;height:47px}
.video-frame{left:633px;top:2202px;width:442px;height:295px;border:5px solid var(--teal);border-radius:0 22px 0 22px}
.video-still{left:612px;top:2184px;width:434px;height:286px;border-radius:0 22px 0 22px;background:linear-gradient(120deg,#3a3d42,#6f6a66 45%,#4a4d52)}
.play{left:809px;top:2307px;width:40px;height:40px;border-radius:50%;background:var(--white);display:flex;align-items:center;justify-content:center}

/* testimonial */
.quote-open{left:176px;top:2740px;font-size:72px;font-weight:700;color:var(--teal);font-style:italic;line-height:1}
.quote-text{left:220px;top:2768px;width:520px;font-size:20px;font-style:italic;color:var(--ink);line-height:1.5}
.quote-close{left:462px;top:2900px;font-size:72px;font-weight:700;color:var(--teal);font-style:italic;line-height:1}
.quote-name{left:211px;top:2946px;font-size:26px;font-weight:500;color:var(--teal)}
.person-photo{left:777px;top:2750px;width:228px;height:228px;border-radius:50%;background:radial-gradient(circle at 50% 45%,#d9d4cf,#a8a5a3)}
.quote-badge{left:931px;top:2890px;width:90px;height:90px;border-radius:50%;background:var(--teal);display:flex;align-items:center;justify-content:center}

/* contact */
.contact-wave{left:0;top:3100px}
.contact-texture{left:0;top:3180px;width:1200px;height:680px;background:radial-gradient(ellipse at 45% 55%,rgba(0,30,35,.22),rgba(0,0,0,0) 60%)}
.contact-title{left:197px;top:3355px;font-size:48px;color:var(--white)}
.contact-text{left:200px;top:3425px;width:400px;font-size:14.5px;color:var(--white)}
.contact-list{left:197px;top:3550px;color:var(--white);font-size:14px;list-style:none}
.contact-list li{display:flex;align-items:center;gap:14px;margin-bottom:14px}
.contact-list .ci{width:36px;height:36px;border-radius:8px;background:var(--sky);display:flex;align-items:center;justify-content:center;flex:none}
.field{left:693px;width:320px;border:2px solid var(--white);color:var(--white);font-size:12px;display:flex;align-items:flex-start;gap:8px;padding:14px 12px}
.submit-btn{left:796px;top:3618px;width:121px;height:44px;font-size:14px}

/* footer */
.site-footer .brand{position:absolute;left:0;top:3920px;width:1200px;justify-content:center}
.footer-nav{left:0;top:4006px;width:1200px;justify-content:center;color:var(--teal)}
.footer-nav a{margin:0 26px}
.copyright{left:0;top:4045px;width:1200px;text-align:center;font-size:15px;color:var(--ink)}
.social{left:0;top:4082px;width:1200px;display:flex;justify-content:center;gap:22px}
.social span{width:24px;height:24px;border-radius:50%;background:var(--teal)}
</style>
</head>
<body>

<!-- Hero -->
<div class="abs hero-photo" role="img" aria-label="Photo of a therapist with a clipboard talking with a client on a sofa in a bright room"></div>
<svg class="abs" style="left:0;top:640px" width="1200" height="220" viewBox="0 0 1200 220">
  <path d="M0 95 C200 60 420 80 620 130 C820 175 1000 170 1200 110 L1200 220 L0 220 Z" fill="#fff"/>
  <path d="M80 85 C300 55 520 95 720 150 C880 190 1020 185 1100 155 C1000 195 860 200 720 168 C520 120 300 80 80 85 Z" fill="#b3dce6"/>
</svg>

<header class="abs site-header">
  <div class="brand"><span>Still Harbor</span><span class="brand-dot"></span></div>
  <nav class="nav">
    <a href="#">Home</a><a href="#">About Us</a><a href="#">Solutions</a><a href="#">Podacast</a><a href="#">News</a><a href="#">Contact</a>
  </nav>
  <a class="btn btn-dark quote-btn" href="#">Get a quote</a>
</header>

<div class="abs hero-circle">
  <h1>Still<br>Harbor</h1>
  <a class="btn btn-light" href="#">get in contact</a>
</div>

<!-- About -->
<section>
  <div class="abs about-bg"></div>
  <div class="abs about-photo photo" role="img" aria-label="Photo of a therapy session with two women seated on a sofa and an armchair"></div>
  <h2 class="abs about-title">About Us</h2>
  <p class="abs about-text">Lorem ipsum dolor sit amet, consectetur adipiscing elit, sed do eiusmod tempor incididunt ut labore et dolore magna aliqua. Quis ipsum suspendisse ultrices gravida. Risus commodo viverra maec enas accumsan lacus vel facilisis.Lorem ipsum dolor sit amet, consectetur adipiscing elit, sed do eiusmod tempor incididunt ut labore et dolore magna aliqua. Quis ipsum suspendisse ultrices gravida. Risus commodo viverra maecenas accumsan lacus vel facilisis. Lorem ipsum dolor sit amet, consectetur adipiscing elit, sed do eiusmod tempor incididunt ut labore et dolore magna aliqua. Quis ipsum suspendisse ultrices gravida.</p>
  <a class="abs btn btn-dark about-btn" href="#">Read more</a>
</section>

<!-- Solutions -->
<section>
  <h2 class="abs sol-title">Our Solutions</h2>
  <p class="abs sol-text">Lorem ipsum dolor sit amet, consectetur adipiscing elit, sed do eiusmod tempor incididunt ut labore et dolore magna aliqua. Quis ipsum suspendisse ultrices gravida. Risus commodo viverra maec&nbsp; enas accumsan lacus vel facilisis.Lorem ipsum dolor sit amet, consectetur adipiscing elit</p>

  <div class="abs sol-card sol-left" style="left:214px;top:1730px">
    <h3>Solution Name</h3>
    <p>Lorem ipsum dolor sit amet, con sec tetur adipiscin lorel sed</p>
    <div class="icon light"><svg width="40" height="40" viewBox="0 0 40 40" fill="none" stroke="#0d5a63" stroke-width="2"><path d="M12 34v-7c-4-3-5-7-4-11 2-6 8-9 14-7 5 2 8 7 6 12l3 5h-4v5h-6v3"/><circle cx="19" cy="17" r="5"/></svg></div>
  </div>
  <div class="abs sol-card sol-right" style="left:620px;top:1730px">
    <h3>Solution Name</h3>
    <p>Lorem ipsum dolor sit amet, con sec tetur adipiscin lorel sed</p>
    <div class="icon dark"><svg width="40" height="40" viewBox="0 0 40 40" fill="none" stroke="#fff" stroke-width="2"><circle cx="20" cy="13" r="6"/><path d="M9 36v-8c0-4 5-7 11-7s11 3 11 7v8"/><rect x="16" y="27" width="8" height="6"/></svg></div>
  </div>
  <div class="abs sol-card sol-left" style="left:214px;top:1874px">
    <h3>Solution Name</h3>
    <p>Lorem ipsum dolor sit amet, con sec tetur adipiscin lorel sed</p>
    <div class="icon dark"><svg width="40" height="40" viewBox="0 0 40 40" fill="none" stroke="#fff" stroke-width="2"><circle cx="20" cy="20" r="4"/><ellipse cx="20" cy="20" rx="14" ry="6"/><ellipse cx="20" cy="20" rx="14" ry="6" transform="rotate(60 20 20)"/><ellipse cx="20" cy="20" rx="14" ry="6" transform="rotate(-60 20 20)"/></svg></div>
  </div>
  <div class="abs sol-card sol-right" style="left:620px;top:1874px">
    <h3>Solution Name</h3>
    <p>Lorem ipsum dolor sit amet, con sec tetur adipiscin lorel sed</p>
    <div class="icon light"><svg width="40" height="40" viewBox="0 0 40 40" fill="none" stroke="#0d5a63" stroke-width="2"><circle cx="22" cy="12" r="7"/><path d="M22 8v4l3 2"/><path d="M5 30l7-6h8l4 3h-8M12 34h12l10-9"/></svg></div>
  </div>
</section>

<!-- Video -->
<section>
  <div class="abs video-bg"></div>
  <h2 class="abs video-title">Our Video</h2>
  <p class="abs video-text">Lorem ipsum dolor sit amet, consectetur adipiscing elit, sed do eiusmod tempor incididunt ut labore et dolore magna aliqua. Quis ipsum suspendisse ultrices gravida. Risus commodo viverra maec&nbsp; enas accumsan lacus vel facilisis.Lorem ipsum dolor sit amet, consectetur adipiscingerra maec&nbsp; enas ac.</p>
  <a class="abs btn btn-dark video-btn" href="#">get in touch</a>
  <div class="abs video-frame"></div>
  <div class="abs video-still" role="img" aria-label="Video still of a counselling conversation between two women in a dark room"></div>
  <div class="abs play"><svg width="16" height="18" viewBox="0 0 16 18"><path d="M2 1l13 8-13 8z" fill="#1d2b3a"/></svg></div>
</section>

<!-- Testimonial -->
<section>
  <div class="abs quote-open">“</div>
  <p class="abs quote-text">Lorem ipsum dolor sit amet, consectetur adipiscing elit, sed do eiusmod tempor incididunt ut labore et dolore magna aliqua. Quis ipsum suspendisse ultrices gravida. Risus commodo viverra maecenas accu msan lacus vel facilisis.</p>
  <div class="abs quote-close">”</div>
  <div class="abs quote-name">Mara Ellison</div>
  <div class="abs person-photo" role="img" aria-label="Portrait photo of the smiling client giving the testimonial"></div>
  <div class="abs quote-badge"><svg width="46" height="36" viewBox="0 0 46 36" fill="#0a4c54"><path d="M0 36V20C0 8 6 2 18 0v7c-6 2-8 5-8 11h8v18zM26 36V20C26 8 32 2 44 0v7c-6 2-8 5-8 11h8v18z"/></svg></div>
</section>

<!-- Contact -->
<section>
  <svg class="abs contact-wave" width="1200" height="780" viewBox="0 0 1200 780">
    <path d="M20 105 C260 40 520 55 760 80 C870 92 950 100 1000 100 C900 112 820 110 740 98 C520 70 260 60 20 105 Z" fill="#b3dce6"/>
    <path d="M0 98 C300 120 520 120 740 110 C960 100 1100 90 1200 75 L1200 710 C1000 740 800 760 600 758 C400 756 200 735 0 700 Z" fill="#0d5a63"/>
  </svg>
  <div class="abs contact-texture" role="img" aria-label="Faint photo of a person with raised arms in a meadow"></div>
  <h2 class="abs contact-title">Contact us</h2>
  <p class="abs contact-text">Lorem ipsum dolor sit amet, consectetur adipis cing elit, sed do eiusmod tempor incididut labore et dolore magna aliquaviverra.</p>
  <ul class="abs contact-list">
    <li><span class="ci"><svg width="16" height="20" viewBox="0 0 16 20"><path d="M8 0a7 7 0 0 1 7 7c0 5-7 13-7 13S1 12 1 7a7 7 0 0 1 7-7z" fill="#0d5a63"/><circle cx="8" cy="7" r="2.5" fill="#b3dce6"/></svg></span><span>1280 Quiet Bay Road, Ste. 210<br>Harborview, FL 33411</span></li>
    <li><span class="ci"><svg width="18" height="18" viewBox="0 0 24 24"><path d="M6 2l4 5-2 3c1 3 3 5 6 6l3-2 5 4-3 4C10 22 2 14 2 5z" fill="#0d5a63"/></svg></span><span>Ph: 555-018-2290</span></li>
    <li><span class="ci"><svg width="18" height="18" viewBox="0 0 20 20" fill="#0d5a63"><rect x="2" y="6" width="16" height="12" rx="2"/><rect x="5" y="1" width="10" height="6" fill="none" stroke="#0d5a63" stroke-width="2"/><rect x="5" y="10" width="10" height="2" fill="#b3dce6"/></svg></span><span>Fax: 555-018-2291</span></li>
  </ul>

  <form>
    <div class="abs field" style="top:3362px;height:47px"><svg width="11" height="11" viewBox="0 0 12 12" fill="#fff"><circle cx="6" cy="3.5" r="3"/><path d="M0 12c0-4 3-5 6-5s6 1 6 5z"/></svg>First Name</div>
    <div class="abs field" style="top:3417px;height:47px"><svg width="11" height="11" viewBox="0 0 12 10" fill="#fff"><rect width="12" height="10" rx="1"/><path d="M0 1l6 5 6-5" stroke="#0d5a63" fill="none"/></svg>Email</div>
    <div class="abs field" style="top:3472px;height:47px"><svg width="11" height="11" viewBox="0 0 24 24" fill="#fff"><path d="M6 2l4 5-2 3c1 3 3 5 6 6l3-2 5 4-3 4C10 22 2 14 2 5z"/></svg>Phone</div>
    <div class="abs field" style="top:3528px;height:116px"><svg width="11" height="11" viewBox="0 0 12 12" fill="#fff"><path d="M0 12l1-4 7-7 3 3-7 7z"/></svg>Message</div>
    <a class="abs btn btn-light submit-btn" href="#">Submit</a>
  </form>
</section>

<!-- Footer -->
<footer class="site-footer">
  <div class="brand"><span>Still Harbor</span><span class="brand-dot"></span></div>
  <nav class="abs nav footer-nav">
    <a href="#">Home</a><a href="#">About Us</a><a href="#">Solutions</a><a href="#">Podacast</a><a href="#">News</a><a href="#">Contact</a>
  </nav>
  <p class="abs copyright">Copyright © 2023 Still Harbor. All rights Reserved</p>
  <div class="abs social"><span></span><span></span><span></span></div>
</footer>

</body>
</html>
```